Sales/Landing Page Redesign for Hunting product

I am looking for a redesign for https://trelwickgear.com/quarter-pad .

We want to add in the information for our new XL quarterpad found: https://trelwickgear.com/shop/hunting/xl-big-game-quarter-pad/

We also will be adding a spot for this video: https://www.vidnorla.com/watch?v=QzR8kLw3hTn

We like having the 3 options at the bottom, but the goal for this page is to sell the quarter pad.

Target Market(s)

Western Hunters, campers, outdoorsmen

Industry/Entity Type

Hunting

Number of Pages Required

1 page

Font styles to use
Sans Serif

Requirements
Must have
• a clean design that is geared to sell the product.

```html
<!DOCTYPE html>
<html lang="en">
<head>
<meta charset="utf-8">
<title>Trelwick Quarter Pads</title>
<link rel="stylesheet" href="https://fonts.googleapis.com/css2?family=Audiowide&family=Barlow:wght@400;500&display=swap">
<style>
:root{
  --red:#e3051b;
  --red-deep:#c90416;
  --black:#151515;
  --ink:#2a2a2a;
  --grey-bg:#f4f4f4;
  --white:#ffffff;
  --line:#e2e2e2;
  --seal-light:#f0d48a;
  --seal-dark:#c9972f;
}
*{margin:0;padding:0;box-sizing:border-box}
html,body{width:1200px;height:3681px;overflow:hidden;background:var(--white)}
body{font-family:"Barlow",sans-serif;color:var(--ink);position:relative}
.display{font-family:"Audiowide",sans-serif;text-transform:uppercase}
section,header,footer{position:absolute;left:0;width:1200px}
.abs{position:absolute}
.rule{position:absolute;height:2px;width:60px;background:var(--red)}
.btn{position:absolute;display:flex;align-items:center;justify-content:center;background:var(--red);color:var(--white);border-radius:32px;font-family:"Audiowide",sans-serif;text-transform:uppercase;font-size:17px;text-decoration:none}
.red{color:var(--red)}

/* header */
.site-header{top:0;height:124px;background:var(--red)}
.site-header svg{position:absolute;left:0;top:0}
.brand{position:absolute;left:111px;top:42px;font-family:"Audiowide",sans-serif;font-size:32px;color:var(--white);letter-spacing:1px}
.nav{position:absolute;top:52px;font-family:"Audiowide",sans-serif;font-size:14px;color:var(--white);text-transform:uppercase}
.cart{position:absolute;left:1026px;top:30px;width:62px;height:62px;border-radius:50%;background:var(--black)}
.cart span{position:absolute;top:8px;width:100%;text-align:center;color:var(--white);font-size:12px}

/* hero */
.hero{top:124px;height:656px;background:linear-gradient(180deg,#3a3d3e 0%,#4b4a40 35%,#6a4a2a 62%,#8a4a1d 78%,#3a2c20 100%)}
.hero-title{position:absolute;top:122px;width:100%;text-align:center;color:var(--white);font-size:40px;line-height:57px}
.hero-sub{position:absolute;top:254px;width:100%;text-align:center;color:var(--red);font-family:"Audiowide",sans-serif;font-size:16px;text-transform:uppercase}

/* welcome */
.welcome{top:780px;height:434px}
.sec-title{position:absolute;width:100%;text-align:center;font-size:36px;color:var(--ink)}
.welcome p{position:absolute;left:210px;width:780px;top:152px;text-align:center;font-size:14px;line-height:32px;color:#444}

/* video block */
.still{top:1214px;height:546px;background:var(--grey-bg)}
.video{position:absolute;left:111px;top:65px;width:528px;height:402px;background:linear-gradient(135deg,#8d9087 0%,#5d6552 55%,#3c4233 100%)}
.play{position:absolute}
.still h2{position:absolute;left:688px;top:92px;font-size:29px;color:var(--ink)}
.checks{position:absolute;left:694px;top:168px;list-style:none}
.checks li{height:45.3px;font-size:16px;color:#333;display:flex;align-items:flex-start;gap:18px}

/* products */
.choose{top:1760px;height:550px}
.card{position:absolute;top:157px;width:234px;height:336px;border:2px solid var(--line);text-align:center}
.card .pic{position:absolute;left:48px;top:34px;width:136px;height:150px;border-radius:24px 24px 18px 18px}
.card .name{position:absolute;top:226px;width:100%;font-size:22px;color:var(--ink)}
.card .kind{position:absolute;top:256px;width:100%;font-size:15px;color:var(--ink)}
.card .price{position:absolute;top:284px;width:100%;font-size:16px;color:var(--red)}

/* testimonials */
.voices{top:2310px;height:578px;background:linear-gradient(180deg,var(--red) 0%,var(--red-deep) 100%)}
.voices .sec-title{color:var(--white)}
.quote{position:absolute;top:155px;width:312px;height:336px;border:2px solid var(--white);color:var(--white)}
.quote svg{position:absolute;left:20px;top:24px}
.quote p{position:absolute;left:22px;top:80px;width:268px;font-size:13px;line-height:26px;text-align:justify}
.quote .who{position:absolute;left:24px;top:252px;font-family:"Audiowide",sans-serif;font-size:14px;text-transform:uppercase}
.quote .stars{position:absolute;left:24px;top:278px;font-size:14px;letter-spacing:3px}

/* guarantee */
.guarantee{top:2888px;height:452px}
.seal-area{position:absolute;left:164px;top:62px;width:336px;height:336px;border-radius:12px;background:linear-gradient(160deg,var(--seal-light) 0%,var(--seal-dark) 100%)}
.guarantee h2{position:absolute;left:562px;top:148px;font-size:28px;color:var(--ink)}
.guarantee .rule{left:570px;top:198px}
.guarantee p{position:absolute;left:571px;top:220px;width:460px;font-size:15px;line-height:29px;color:#444}

/* footer */
.site-footer{top:3340px;height:341px;background:var(--black)}
.site-footer svg.wedge{position:absolute;left:0;top:0}
.foot-brand{position:absolute;top:44px;width:100%;text-align:center;font-family:"Audiowide",sans-serif;font-size:34px;color:var(--white)}
.foot-links{position:absolute;top:142px;width:100%;text-align:center;font-size:12px;font-weight:500;color:var(--white);text-transform:uppercase;letter-spacing:.3px}
.foot-links span{margin:0 12px}
.socials{position:absolute;top:202px;left:510px;display:flex;gap:11px}
.socials i{display:block;width:37px;height:37px;border-radius:50%;background:var(--red)}
.foot-rule{position:absolute;top:260px;left:205px;width:884px;height:1px;background:#3a3a3a}
.copy{position:absolute;top:290px;width:100%;text-align:center;font-size:15px;color:var(--white)}
.ver{position:absolute;left:1105px;top:296px;font-size:14px;color:#ddd}
</style>
</head>
<body>

<header class="site-header">
  <svg width="420" height="124"><polygon points="0,0 412,0 370,124 0,124" fill="#151515"/></svg>
  <div class="brand">TRELWICK</div>
  <a class="nav" style="left:559px">Home</a>
  <a class="nav" style="left:645px">Meals</a>
  <a class="nav" style="left:741px">Quarter Pads</a>
  <a class="nav" style="left:909px">Contact Us</a>
  <div class="cart"><span>0</span>
    <svg class="abs" style="left:21px;top:25px" width="20" height="18" viewBox="0 0 20 18"><path d="M0 1h4l3 10h10l2-7H6" fill="none" stroke="#fff" stroke-width="2"/><circle cx="8" cy="15" r="2" fill="#fff"/><circle cx="16" cy="15" r="2" fill="#fff"/></svg>
  </div>
</header>

<section class="hero" role="img" aria-label="Hunter at dusk beside game meat laid out on an orange quarter pad on a hillside">
  <h1 class="hero-title display">Quarter Pads<br>To Keep Your Meat Clean</h1>
  <div class="hero-sub">100% Waterproof · Lightweight · Quality Guarantee</div>
  <a class="btn" style="left:505px;top:301px;width:190px;height:60px">Buy Now</a>
</section>

<section class="welcome">
  <h2 class="sec-title display" style="top:68px">Welcome <span class="red">Trelwick</span></h2>
  <div class="rule" style="left:570px;top:132px"></div>
  <p>Thank you for your support! We truly appreciate your business, and your love of the outdoors! Because of extreme demand for our meals during this pandemic, all meals are currently on backorder.Stay updated about the availability of our delicious meals, by signing-up for our newsletter. You can even place an order and they will be shipped out in the order they are received. Thanks for being a part of the Trelwick Family!</p>
  <a class="btn" style="left:490px;top:314px;width:220px;height:63px">Read More</a>
</section>

<section class="still">
  <div class="video" role="img" aria-label="Video still of a hunter in camouflage in the field">
    <svg class="play" width="90" height="90" viewBox="0 0 90 90" style="left:219px;top:156px"><circle cx="45" cy="45" r="43" fill="none" stroke="#fff" stroke-width="3"/><polygon points="35,28 35,62 63,45" fill="#fff"/></svg>
  </div>
  <h2 class="display">Do You Still...</h2>
  <div class="rule" style="left:690px;top:138px;width:50px"></div>
  <ul class="checks">
    <li><svg width="16" height="16" viewBox="0 0 16 16" style="margin-top:3px"><circle cx="8" cy="8" r="6.5" fill="none" stroke="#e3051b" stroke-width="2"/><path d="M5 8l2.2 2.2L11 6" fill="none" stroke="#e3051b" stroke-width="2"/></svg>Lay Your Fresh Meat On A Rock?</li>
    <li><svg width="16" height="16" viewBox="0 0 16 16" style="margin-top:3px"><circle cx="8" cy="8" r="6.5" fill="none" stroke="#e3051b" stroke-width="2"/><path d="M5 8l2.2 2.2L11 6" fill="none" stroke="#e3051b" stroke-width="2"/></svg>Sew Bed Sheets Together?</li>
    <li><svg width="16" height="16" viewBox="0 0 16 16" style="margin-top:3px"><circle cx="8" cy="8" r="6.5" fill="none" stroke="#e3051b" stroke-width="2"/><path d="M5 8l2.2 2.2L11 6" fill="none" stroke="#e3051b" stroke-width="2"/></svg>Use A Blue Tarp?</li>
    <li><svg width="16" height="16" viewBox="0 0 16 16" style="margin-top:3px"><circle cx="8" cy="8" r="6.5" fill="none" stroke="#e3051b" stroke-width="2"/><path d="M5 8l2.2 2.2L11 6" fill="none" stroke="#e3051b" stroke-width="2"/></svg>Lay Your Meat In The Dirt?</li>
    <li><svg width="16" height="16" viewBox="0 0 16 16" style="margin-top:3px"><circle cx="8" cy="8" r="6.5" fill="none" stroke="#e3051b" stroke-width="2"/><path d="M5 8l2.2 2.2L11 6" fill="none" stroke="#e3051b" stroke-width="2"/></svg>Stuff The Meat In Old Used Pillow Cases?</li>
  </ul>
  <a class="btn" style="left:692px;top:408px;width:302px;height:52px">Select My Quarter Pad</a>
</section>

<section class="choose">
  <h2 class="sec-title display" style="top:52px">Choose Your <span class="red">Quarter Pad</span></h2>
  <div class="rule" style="left:570px;top:116px"></div>
  <div class="card" style="left:111px">
    <div class="pic" role="img" aria-label="Red quarter pad in stuff sack" style="background:linear-gradient(160deg,#e0242c,#a9121a)"></div>
    <div class="name display">Red</div><div class="kind display">Quarter Pad</div><div class="price display">$19.99</div>
  </div>
  <div class="card" style="left:359px">
    <div class="pic" role="img" aria-label="Orange quarter pad in stuff sack" style="background:linear-gradient(160deg,#ff7a2e,#ea5a12)"></div>
    <div class="name display">Orange</div><div class="kind display">Quarter Pad</div><div class="price display">$19.99</div>
  </div>
  <div class="card" style="left:606px">
    <div class="pic" role="img" aria-label="Green quarter pad in stuff sack" style="background:linear-gradient(160deg,#2fc25a,#14963c)"></div>
    <div class="name display">Green</div><div class="kind display">Quarter Pad</div><div class="price display">$19.99</div>
  </div>
  <div class="card" style="left:854px">
    <div class="pic" role="img" aria-label="XL big game quarter pad in orange stuff sack" style="background:linear-gradient(160deg,#ff7a2e,#ea5a12)"></div>
    <div class="name display">XL Big Game</div><div class="kind display">Quarter Pad</div><div class="price display">$29.99</div>
  </div>
</section>

<section class="voices">
  <h2 class="sec-title display" style="top:62px">What Others Are Saying...</h2>
  <div class="rule" style="left:570px;top:126px;background:#fff"></div>
  <div class="quote" style="left:111px">
    <svg width="34" height="28" viewBox="0 0 34 28"><path d="M0 28V15C0 6 5 1 13 0v5c-4 1-6 4-6 8h6v15zM19 28V15c0-9 5-14 13-15v5c-4 1-6 4-6 8h6v15z" fill="#fff"/></svg>
    <p>Gone are the days of struggling to keep a quarter from sliding off a log or rock while trying to de-bone meat. Packs small, weighs nothing, and keeps meat perfectly clean. It's in my pack 100% of the time. Great Product!</p>
    <div class="who">Marlow Keats</div><div class="stars">☆☆☆☆☆</div>
  </div>
  <div class="quote" style="left:444px">
    <svg width="34" height="28" viewBox="0 0 34 28"><path d="M0 28V15C0 6 5 1 13 0v5c-4 1-6 4-6 8h6v15zM19 28V15c0-9 5-14 13-15v5c-4 1-6 4-6 8h6v15z" fill="#fff"/></svg>
    <p>he Quarter Pads keep your meat clean and double up as a waterproof poncho and ground tarp. They are a must have for any serious hunter.he Quarter Pads keep your meat clean and double up as a waterproof poncho and ground tarp.</p>
    <div class="who">Dell Amberly</div><div class="stars">☆☆☆☆☆</div>
  </div>
  <div class="quote" style="left:777px">
    <svg width="34" height="28" viewBox="0 0 34 28"><path d="M0 28V15C0 6 5 1 13 0v5c-4 1-6 4-6 8h6v15zM19 28V15c0-9 5-14 13-15v5c-4 1-6 4-6 8h6v15z" fill="#fff"/></svg>
    <p>The Quarter Pad is a game changer when it comes to cleanliness in the hills. Light-weight, and compacts down super small! No more getting dirt and pine needles all over your meat.</p>
    <div class="who">Rhett Calloway</div><div class="stars">☆☆☆☆☆</div>
  </div>
</section>

<section class="guarantee">
  <div class="seal-area" role="img" aria-label="Quality guarantee seal badge"></div>
  <h2 class="display">100% Quality Guarantee</h2>
  <div class="rule"></div>
  <p>We've designed our Quarter Pads for maximum performance and durability so you can keep the meat you harvest in the backcountry clean and out of the dirt. If you are at all unsatisfied, contact us and we'll make it right.</p>
</section>

<footer class="site-footer">
  <svg class="wedge" width="300" height="341"><polygon points="0,0 28,0 300,341 0,341" fill="#c90416"/></svg>
  <div class="foot-brand">TRELWICK</div>
  <div class="foot-links">My Account<span>/</span>Blog<span>/</span>Terms of Service Agreement<span>/</span>Refund &amp; Return Policy<span>/</span>Privacy Policy Agreement</div>
  <div class="socials"><i></i><i></i><i></i><i></i></div>
  <div class="foot-rule"></div>
  <div class="copy">©2020 Trelwick. All rights reserved.</div>
  <div class="ver">C2</div>
</footer>

</body>
</html>
```